Fontenot Bayou Grillhouse (Owners Card)

Need a classy, but modern business card. I have included a promotional card for the steakhouse. I need one for myself (the owner) that is more professional.

Target Market(s)

General Public

Industry/Entity Type

Food service

Contact Information for Business Card

Name, business address, phone number, email, logo

Font styles to use
Serif
Sans Serif
Decorative
Script

Requirements
Must have
• My name (Darvel Pruitt), business address (327 Oakmere Street), phone number (510) 493-2615, email (Dpruittkr4@mailvane.example. On the back of the card: Psalms 27 1 The LORD is my light and my salvation— whom shall I fear? The LORD is the stronghold of my life— of whom shall I be afraid? 2 When the wicked advance against me to devour me, it is my enemies and my foes who will stumble and fall. 3 Though an army besiege me, my heart will not fear; though war break out against me, even then I will be confident.
Nice to have
• Something that’s bold, but modern and professional.

```html
<!DOCTYPE html>
<html lang="en">
<head>
<meta charset="utf-8">
<title>Fontenot Bayou Grillhouse – Owner Card</title>
<link rel="stylesheet" href="https://fonts.googleapis.com/css2?family=Cinzel:wght@600;700&family=Cormorant+Garamond:wght@500&family=Poppins:wght@400;500&display=swap">
<style>
  :root {
    --backdrop: #737373;
    --lime: #19f50f;
    --gold: #e6b800;
    --orange: #ff8a00;
    --red: #ff1a0a;
    --white: #ffffff;
    --ivory: #efe8e1;
    --ink: #2b2522;
    --taupe: #c8bcb1;
    --watermark-light: rgba(150, 135, 125, 0.22);
    --watermark-warm: rgba(110, 170, 20, 0.55);
  }
  * { margin: 0; padding: 0; box-sizing: border-box; }
  html, body { width: 1200px; height: 1000px; overflow: hidden; }
  body { background: var(--backdrop); position: relative; font-family: "Poppins", sans-serif; }

  .card {
    position: absolute;
    left: 294px;
    width: 612px;
    height: 352px;
    border-radius: 28px;
    overflow: hidden;
  }
  .card--front {
    top: 133px;
    background: linear-gradient(100deg, var(--lime) 0%, var(--gold) 30%, var(--orange) 55%, #ff5a00 80%, var(--red) 100%);
  }
  .card--back { top: 517px; background: var(--ivory); }

  .decor-mask-area { position: absolute; left: 368px; top: 0; width: 244px; height: 205px; }

  .front-watermark {
    position: absolute;
    left: 268px;
    top: 226px;
    font-family: "Cinzel", serif;
    font-weight: 700;
    font-size: 62px;
    line-height: 62px;
    color: var(--watermark-warm);
    white-space: nowrap;
  }

  .brand {
    position: absolute;
    left: 58px;
    top: 54px;
    display: flex;
    align-items: center;
    gap: 12px;
  }
  .brand__dot { width: 40px; height: 40px; border-radius: 50%; background: var(--white); }
  .brand__name {
    font-family: "Cinzel", serif;
    font-weight: 700;
    font-size: 19px;
    line-height: 21px;
    color: var(--white);
  }

  .owner {
    position: absolute;
    left: 16px;
    width: 360px;
    text-align: center;
    color: var(--white);
  }
  .owner__name { top: 140px; font-family: "Cinzel", serif; font-weight: 700; font-size: 24px; }
  .owner__title { top: 169px; font-size: 15px; letter-spacing: 1px; font-weight: 500; }
  .owner__icons { top: 202px; display: flex; justify-content: center; gap: 6px; }
  .icon { width: 32px; height: 32px; border-radius: 50%; background: var(--white); display: flex; align-items: center; justify-content: center; }
  .owner__phone { top: 236px; font-size: 17px; }
  .owner__email { top: 259px; font-size: 17px; }
  .owner__address { top: 306px; font-size: 13.5px; }

  .verse-title {
    position: absolute;
    top: 30px;
    width: 100%;
    text-align: center;
    font-family: "Cinzel", serif;
    font-weight: 600;
    font-size: 25px;
    color: var(--taupe);
  }
  .verse {
    position: absolute;
    top: 74px;
    width: 100%;
    text-align: center;
    font-family: "Cormorant Garamond", serif;
    font-weight: 500;
    font-size: 17px;
    line-height: 20.5px;
    color: var(--ink);
  }
  .back-watermark {
    position: absolute;
    left: -4px;
    top: 236px;
    font-family: "Cinzel", serif;
    font-weight: 700;
    font-size: 66px;
    line-height: 70px;
    color: var(--watermark-light);
    white-space: nowrap;
  }
</style>
</head>
<body>
  <section class="card card--front">
    <svg class="decor-mask-area" role="img" aria-label="Large ornamental carnival mask with feathered plume, decorative" viewBox="0 0 244 205">
      <defs>
        <linearGradient id="maskTone" x1="0" y1="0" x2="1" y2="1">
          <stop offset="0" stop-color="#7ac60a" stop-opacity="0.75"/>
          <stop offset="1" stop-color="#c23800" stop-opacity="0.55"/>
        </linearGradient>
      </defs>
      <ellipse cx="150" cy="105" rx="150" ry="105" fill="url(#maskTone)" opacity="0.6"/>
    </svg>

    <div class="front-watermark">FONTENOT BAYOU<br>GRILLHOUSE</div>

    <div class="brand">
      <span class="brand__dot"></span>
      <span class="brand__name">Fontenot Bayou<br>Grillhouse</span>
    </div>

    <div class="owner owner__name">Darvel Pruitt</div>
    <div class="owner owner__title">OWNER</div>
    <div class="owner owner__icons">
      <span class="icon">
        <svg width="16" height="16" viewBox="0 0 24 24"><path fill="#ff8a00" d="M6.6 10.8a15.1 15.1 0 0 0 6.6 6.6l2.2-2.2a1 1 0 0 1 1-.25 11.4 11.4 0 0 0 3.6.57 1 1 0 0 1 1 1V20a1 1 0 0 1-1 1A17 17 0 0 1 3 4a1 1 0 0 1 1-1h3.5a1 1 0 0 1 1 1c0 1.25.2 2.45.57 3.57a1 1 0 0 1-.25 1z"/></svg>
      </span>
      <span class="icon">
        <svg width="16" height="16" viewBox="0 0 24 24"><rect x="2.5" y="5" width="19" height="14" rx="1.5" fill="none" stroke="#ff8a00" stroke-width="2"/><path d="M3 6l9 7 9-7" fill="none" stroke="#ff8a00" stroke-width="2"/></svg>
      </span>
    </div>
    <div class="owner owner__phone">(510) 493-2615</div>
    <div class="owner owner__email">Dpruittkr4@mailvane.example</div>
    <div class="owner owner__address">327 Oakmere Street, Larkmoor, CA 94618, EUA</div>
  </section>

  <section class="card card--back">
    <h2 class="verse-title">Psalms 27</h2>
    <p class="verse">
      The LORD is my light and my salvation—<br>
      whom shall I fear? The LORD is the stronghold of my life—<br>
      of whom shall I be afraid? When the wicked advance against<br>
      me to devour me, it is my enemies and my foes<br>
      who will stumble and fall. Though an army<br>
      besiege me, my heart will not fear; though war break out<br>
      against me, even then I will be confident.
    </p>
    <div class="back-watermark">FONTENOT BAYOU<br>GRILLHOUSE</div>
  </section>
</body>
</html>
```